Heronby Mortgage Capital Business Card

We need a business card design for our mortgage servicing company. In addition to servicing the loans of homeowners, we help homeowners with purchasing their homes and any mortgage refinancing. We would like to see designs that use the colors in the logo attached below (gold-ish yellow and navy blue), and any other design you deem fit! The design should communicate a simpler life with smart mortgages provided by Heronby.

```html
<!DOCTYPE html>
<html lang="en">
<head>
<meta charset="utf-8">
<title>Heronby Mortgage Capital – Business Card</title>
<link rel="stylesheet" href="https://fonts.googleapis.com/css2?family=Open+Sans:wght@400;600&display=swap">
<style>
  :root {
    --backdrop: #3f290c;
    --card: #ffffff;
    --gold: #dcae42;
    --gold-light: #e0b246;
    --bronze: #8a5a24;
    --navy: #2a2f66;
    --ink: #343a48;
  }
  * { box-sizing: border-box; margin: 0; padding: 0; }
  html, body {
    width: 1200px; height: 1200px; overflow: hidden;
    background: var(--backdrop);
    font-family: "Open Sans", Arial, sans-serif;
  }
  .canvas { position: relative; width: 1200px; height: 1200px; }
  .card {
    position: absolute; left: 228px; width: 750px; height: 442px;
    background: var(--card); overflow: hidden;
  }
  .card--front { top: 120px; }
  .card--back { top: 638px; }
  .card__accent { position: absolute; inset: 0; width: 100%; height: 100%; }

  .wordmark {
    position: absolute; color: var(--navy); font-weight: 600;
    white-space: nowrap; letter-spacing: 0.5px;
  }
  .card--front .wordmark { left: 45px; top: 64px; font-size: 34px; }
  .card--back .wordmark {
    left: 0; right: 0; top: 200px; text-align: center; font-size: 40px;
  }

  .holder__name {
    position: absolute; left: 45px; top: 158px;
    font-size: 35px; font-weight: 400; color: var(--ink); letter-spacing: 0.3px;
  }
  .holder__role {
    position: absolute; left: 45px; top: 203px;
    font-size: 17px; color: var(--ink);
  }
  .holder__rule {
    position: absolute; left: 45px; top: 237px; width: 46px; height: 2px;
    background: var(--gold);
  }
  .contact { position: absolute; left: 45px; top: 0; list-style: none; }
  .contact__item {
    position: absolute; left: 0; display: flex; align-items: center;
    white-space: nowrap; font-size: 17px; color: var(--ink);
  }
  .contact__item:nth-child(1) { top: 269px; }
  .contact__item:nth-child(2) { top: 315px; }
  .contact__item:nth-child(3) { top: 361px; }
  .contact__icon {
    width: 36px; height: 36px; border-radius: 50%; background: var(--gold);
    display: flex; align-items: center; justify-content: center;
    margin-right: 14px; flex: none;
  }
  .contact__icon svg { width: 20px; height: 20px; }
</style>
</head>
<body>
<main class="canvas">

  <section class="card card--front">
    <svg class="card__accent" viewBox="0 0 750 442" role="img" aria-label="Soft gold gradient crescent accent along the right edge">
      <defs>
        <linearGradient id="front-accent" x1="0" x2="1" y1="0" y2="0">
          <stop offset="0" stop-color="#e0b246"/>
          <stop offset="1" stop-color="#a8702a"/>
        </linearGradient>
      </defs>
      <path fill="url(#front-accent)" d="M700,0 L750,0 C620,110 610,320 750,442 L610,442 C530,300 560,120 700,0 Z"/>
    </svg>

    <p class="wordmark">Heronby Mortgage</p>

    <h1 class="holder__name">Unknown Person</h1>
    <p class="holder__role">Owner/Co Founder</p>
    <span class="holder__rule"></span>

    <ul class="contact">
      <li class="contact__item">
        <span class="contact__icon">
          <svg viewBox="0 0 24 24"><path fill="#fff" d="M6.6 3.5l2.6 3.2c.4.5.4 1.2-.1 1.7L7.8 9.7c.9 2.3 3.3 4.8 5.9 6l1.3-1.3c.5-.5 1.2-.5 1.700-.1l3.2 2.6c.5.4.6 1.2.1 1.7l-1.6 1.8c-.6.7-1.6.9-2.5.6C9.7 19 5 14.3 3.1 8.1c-.3-.9 0-1.9.6-2.5L5 3.4c.5-.5 1.2-.4 1.6.1z"/></svg>
        </span>
        +123-456-7890
      </li>
      <li class="contact__item">
        <span class="contact__icon">
          <svg viewBox="0 0 24 24" fill="none" stroke="#fff" stroke-width="1.6"><circle cx="12" cy="12" r="8"/><path d="M4 12h16M12 4c3 3 3 13 0 16M12 4c-3 3-3 13 0 16"/></svg>
        </span>
        www.reallygreatsite.com
      </li>
      <li class="contact__item">
        <span class="contact__icon">
          <svg viewBox="0 0 24 24"><path fill="#fff" d="M12 2.5c-3.6 0-6.3 2.8-6.3 6.3 0 4.6 6.3 12.7 6.3 12.7s6.3-8.1 6.3-12.7c0-3.5-2.7-6.3-6.3-6.3zm0 8.8a2.5 2.5 0 1 1 0-5 2.5 2.5 0 0 1 0 5z"/></svg>
        </span>
        123 Anywhere St., Any City, ST
      </li>
    </ul>
  </section>

  <section class="card card--back">
    <svg class="card__accent" viewBox="0 0 750 442" role="img" aria-label="Soft gold gradient crescent accents framing the centre">
      <defs>
        <linearGradient id="back-accent-left" x1="0" x2="1" y1="0" y2="0">
          <stop offset="0" stop-color="#e0b246"/>
          <stop offset="1" stop-color="#a8702a"/>
        </linearGradient>
        <linearGradient id="back-accent-right" x1="0" x2="1" y1="0" y2="0">
          <stop offset="0" stop-color="#a8702a"/>
          <stop offset="1" stop-color="#e0b246"/>
        </linearGradient>
      </defs>
      <path fill="url(#back-accent-left)" d="M150,0 L240,0 C120,110 110,330 240,442 L90,442 C20,300 40,120 150,0 Z"/>
      <path fill="url(#back-accent-right)" d="M600,0 L510,0 C630,110 640,330 510,442 L660,442 C730,300 710,120 600,0 Z"/>
    </svg>

    <p class="wordmark">Heronby Mortgage</p>
  </section>

</main>
</body>
</html>
```